Web design for a relaunch of a technology and knowledge transfer company

Design for the relaunch of an existing website The company specializes in technology and knowledge transfer between companies (and universities). The innovation company (company name) combines many years of experience in technology transfer, innovation management, project management and grant applications. Link: http://www.fortschrittswerkhaus.example The colors of the logo are not very advantageous and can be adjusted a bit. There are currently no picture worlds, these are to be selected by the designer. Abstract motifs are certainly an advantage here (10 motifs). Animated programming could be done (network etc. http://valmeta.brixlane.example/). In this case a suggestion is made, which we convert programming technically. The structure and contents of the existing pages will be adopted and supplemented. The programming will be done with TYPO3 in responsive form (bootstrap). Required are start page, content page and contact page. -------------------------------------------------- ------------------------------ Web design for a relaunch of a company in technology and knowledge transfer Design for the relaunch of an existing website. The company specializes in technology and knowledge transfer between companies (and universities). The innovation company combines many years of experience in the fields of technology transfer, innovation management, project management and grant application. Link: http://www.fortschrittswerkhaus.example The color of the logo is not exactly advantageous and can be adjusted. There are currently no image worlds, these are to be selected by the designer. Abstract motifs are certainly an advantage here (10 motifs). It could also be made animated programming (network, etc. http://valmeta.brixlane.example/). In this case, a proposal has to be made, which we implement in terms of programming technology. The structure and contents of the existing pages are taken over and supplemented. Programming is done with TYPO3 in responsive form (bootstrap). Required are homepage, content page and contact page.

```html
<!DOCTYPE html>
<html lang="en">
<head>
<meta charset="utf-8">
<title>Fortschrittswerkhaus – Technology &amp; Knowledge Transfer</title>
<link href="https://fonts.googleapis.com/css2?family=Poppins:wght@300;400;500;600&display=swap" rel="stylesheet">
<style>
:root{
  --page-bg:#efeaea;
  --blue:#2a36b6;
  --blue-light:#3441c4;
  --navy:#141b60;
  --red:#e2182e;
  --white:#ffffff;
  --muted:#c9cdf2;
}
*{box-sizing:border-box;margin:0;padding:0}
html,body{width:1200px;height:2459px;overflow:hidden;background:var(--page-bg);font-family:'Poppins',sans-serif;color:var(--white)}
.site{position:absolute;left:246px;top:191px;width:708px}
section,header,footer{position:relative;width:708px;overflow:hidden}
.abs{position:absolute}
.center{text-align:center;left:0;right:0}

/* hero */
.hero{height:436px;background:radial-gradient(circle at 70% 30%,var(--blue-light),var(--blue) 70%)}
.brand{left:20px;top:50px;display:flex;align-items:center;gap:9px;font-size:11px;font-weight:500}
.brand-mark{width:14px;height:14px;border:1.5px solid var(--white)}
.menu{right:22px;top:54px;width:14px}
.menu span{display:block;height:1.5px;background:var(--white);margin-bottom:3px}
.hero-title{top:116px;font-size:21px;font-weight:600}
.hero-sub{top:150px;font-size:10px;font-weight:300}
.hero-art{left:107px;top:189px;width:492px;height:247px;border-radius:120px 120px 0 0;background:linear-gradient(90deg,#5f8fd8 0%,#d9579f 35%,#e2509a 65%,#5f8fd8 100%);opacity:.85}
.slide-dots{right:28px;top:200px;display:flex;flex-direction:column;gap:14px}
.slide-dots span{width:7px;height:7px;border:1px solid var(--white);border-radius:50%}
.slide-dots span.active{background:var(--white)}
.scroll-down{left:346px;top:396px;width:15px;height:15px;border:1px solid var(--white);border-radius:50%}

/* services */
.services{height:413px;background:linear-gradient(135deg,#8f9aa3,#5d6b76 45%,#3f4850)}
.services-title{top:62px;font-size:21px;font-weight:400}
.service{width:120px;text-align:center;top:230px;font-size:10px;font-weight:500;line-height:1.2}
.service svg{display:block;margin:0 auto 8px}
.btn-outline{border:1px solid var(--white);font-size:8px;font-weight:500;text-align:center}
.services .btn-outline{left:403px;top:326px;width:46px;height:20px;line-height:18px}

/* intro */
.intro{height:407px;background:var(--blue)}
.intro-text{top:60px;font-size:23px;line-height:27.5px;font-weight:400}
.intro-text u{text-decoration-thickness:1px;text-underline-offset:4px}
.intro-sub{top:257px;font-size:10px;font-weight:500}
.btn-red{left:272px;top:309px;width:163px;height:34px;line-height:34px;background:var(--red);font-size:11px;font-weight:600;text-align:center}

/* reports */
.reports{height:410px;background:var(--navy)}
.reports-title{top:60px;font-size:22px;font-weight:400}
.grid{left:66px;top:114px;width:577px;height:231px}
.tile{position:absolute;overflow:hidden}
.photo{background:linear-gradient(160deg,#b9b2a4,#6e6558 60%,#433b32)}
.date{font-size:7px;color:var(--red);font-weight:500}
.tile-title{font-size:9px;font-weight:600;line-height:1.35}
.tile-lead{left:0;top:0;width:288px;height:231px}
.tile-lead .caption{left:20px;top:150px}
.tile-lead .btn-outline{left:20px;top:190px;width:56px;height:20px;line-height:18px}
.tile-mid-photo{left:288px;top:0;width:144px;height:115px;background:linear-gradient(160deg,#6d7690,#2e3547)}
.tile-mid-text{left:288px;top:115px;width:144px;height:116px;background:var(--blue);padding:20px 16px}
.tile-right-text{left:432px;top:0;width:145px;height:115px;background:var(--white);color:#1d2250;padding:20px 16px}
.tile-right-text .tile-title{font-weight:400;font-size:8.5px}
.tile-right-photo{left:432px;top:115px;width:145px;height:116px;background:linear-gradient(160deg,#c2c6cc,#6a717c)}

/* footer */
.contact{height:410px;background:var(--blue)}
.say-hello{left:138px;top:62px;font-size:32px;font-weight:400}
.say-hello span{color:transparent;-webkit-text-stroke:1px var(--muted)}
.contact-col{left:376px;top:68px;font-size:8px;line-height:1.55}
.contact-col h4{font-size:8px;font-weight:600;margin-bottom:8px}
.contact-col .phone{font-size:11px;font-weight:600;margin-bottom:20px}
.contact-col .btn-outline{width:54px;height:22px;line-height:20px;margin-top:16px}
.social{right:28px;top:70px;display:flex;flex-direction:column;gap:14px}
.social span{width:10px;height:10px;border:1.5px solid var(--white)}
.social span.accent{border-color:var(--red)}
.legal{left:138px;top:372px;font-size:7px;font-weight:300}
.legal-links{left:376px;top:372px;font-size:7px;font-weight:300}
.to-top{right:26px;top:366px}
</style>
</head>
<body>
<main class="site">

  <header class="hero">
    <div class="abs brand"><span class="brand-mark"></span>Fortschrittswerkhaus</div>
    <div class="abs menu"><span></span><span></span><span></span></div>
    <h1 class="abs center hero-title">Technology &amp; Knowledge Transfer</h1>
    <p class="abs center hero-sub">that supports companies in implementing their innovative ideas.</p>
    <div class="abs hero-art" role="img" aria-label="Illustration of two heads facing each other, filled with gears exchanging ideas"></div>
    <div class="abs slide-dots"><span class="active"></span><span></span><span></span><span></span><span></span></div>
    <div class="abs scroll-down"></div>
  </header>

  <section class="services">
    <div class="abs" style="inset:0" role="img" aria-label="Photo of a team meeting around a table in a bright office"></div>
    <h2 class="abs center services-title">Our Services</h2>
    <div class="abs service" style="left:78px">
      <svg width="24" height="24" viewBox="0 0 24 24" fill="none" stroke="#fff" stroke-width="1.3"><circle cx="12" cy="12" r="9"/><path d="M8 12h8M13 9l3 3-3 3"/></svg>Technology<br>Transfer</div>
    <div class="abs service" style="left:222px">
      <svg width="24" height="24" viewBox="0 0 24 24" fill="none" stroke="#fff" stroke-width="1.3"><path d="M12 3a6 6 0 0 0-3.5 10.9V17h7v-3.1A6 6 0 0 0 12 3zM9.5 20h5"/></svg>Innovation<br>Management</div>
    <div class="abs service" style="left:366px">
      <svg width="24" height="24" viewBox="0 0 24 24" fill="none" stroke="#fff" stroke-width="1.3"><rect x="3" y="5" width="18" height="14"/><path d="M3 10h18M8 14h8"/></svg>Project<br>Management</div>
    <div class="abs service" style="left:511px">
      <svg width="24" height="24" viewBox="0 0 24 24" fill="none" stroke="#fff" stroke-width="1.3"><rect x="5" y="3" width="14" height="18"/><path d="M8 9l2 2 4-4M8 15h8"/></svg>Grant<br>Application</div>
    <div class="abs btn-outline">More</div>
  </section>

  <section class="intro">
    <p class="abs center intro-text"><u>Fortschrittswerkhaus</u> is a technology<br>and knowledge <u>transfer company</u><br>that <u>supports</u> companies in<br><u>implementing</u> their <u>innovative ideas</u>.<br>We use our large network of<br>scientific institutions.</p>
    <p class="abs center intro-sub">Let's get find the right answers for you and your company!</p>
    <div class="abs btn-red">Contact Us Today!</div>
  </section>

  <section class="reports">
    <h2 class="abs center reports-title">Reports on current topics &amp; events</h2>
    <div class="abs grid">
      <article class="tile tile-lead photo" role="img" aria-label="Photo of a speaker presenting in a lecture hall">
        <div class="abs caption"><p class="date">09.11.2018</p><p class="tile-title">IoT - what companies want</p></div>
        <div class="abs btn-outline">More</div>
      </article>
      <div class="tile tile-mid-photo" role="img" aria-label="Photo of a panel discussion on stage"></div>
      <article class="tile tile-mid-text"><p class="date">05.11.2018</p><p class="tile-title">StartUp Conference on the 5th and 6th of Sep-tember in Bergstedt</p></article>
      <article class="tile tile-right-text"><p class="date">09.10.2018</p><p class="tile-title">In conversation with the Aldstadt Institute</p></article>
      <div class="tile tile-right-photo" role="img" aria-label="Photo of a man in a production hall"></div>
    </div>
  </section>

  <footer class="contact">
    <h2 class="abs say-hello">Say <span>Hello!</span></h2>
    <div class="abs contact-col">
      <h4>Contact Us Today!</h4>
      <p>info@fortschrittswerkhaus.example</p>
      <p class="phone">(+49) 5550 12 34 567</p>
      <h4>Visit Us</h4>
      <p>Werkhaus Society for<br>University &amp; Business Management<br>Lindenweg 7<br>31000 Neustadt</p>
      <div class="btn-outline">Hire Us</div>
    </div>
    <div class="abs social"><span></span><span class="accent"></span><span></span><span></span></div>
    <p class="abs legal">© Copyright 2019. Fortschrittswerkhaus</p>
    <p class="abs legal-links">Imprint &nbsp;Data Protection</p>
    <svg class="abs to-top" width="12" height="14" viewBox="0 0 12 14" fill="none" stroke="#fff" stroke-width="1.3"><path d="M6 13V1M1 6l5-5 5 5"/></svg>
  </footer>

</main>
</body>
</html>
```